My Bramblewood Interiors llc fliers project

A flyer that will be direct mailed to customers. feel free to play with wording this is what i have now. I wlil include every service i offer in must haves and feel free to run a footer stating all my services
" My background, I'm Oren Vashtakar, I was born Into this business, Its what I know. So if your tired of waiting for weeks before your kitchen gets completed, as happens with other companies. If your tired of dealing with unreliable contractors deal with me. I'm so confident in my work, here are the numbers to previous customer. Mrs.Pelham-703-555-0142. Mr.Castellano 703-555-0187. They will tell you I can provide you that dream kitchen and countertop installed, within a week. Mention this flyer to receive an additional 10% discoun
BrambleWood Interiors llc
5819 fernwick dale CT
Falls church VA,22042
703-555-0163
Ovashtakar@mailbrook.net"

Target Market(s)

high income household income looking to get interior work done,

Industry/Entity Type

Church

Font styles to use
Serif

Requirements
Must have
• granite and marble kitchen and bathroom fabrication and install
• any flooring, hardwood, marble, carpet, laminate, install
• Kitchen cabinet design and install
• Bathroom remodeling
Nice to have
• an easy to read flyer that will give customers the info to reach me and understand what they do, if I put to much then reduce it.

```html
<!DOCTYPE html>
<html lang="en">
<head>
<meta charset="utf-8">
<title>BrambleWood Interiors llc – Postcard</title>
<link href="https://fonts.googleapis.com/css2?family=Arimo:ital,wght@0,400;0,700;1,400;1,700&display=swap" rel="stylesheet">
<style>
  :root {
    --brand-blue: #1a8fd6;
    --deep-blue: #0d6fb8;
    --ink: #1d1d1d;
    --logo-ink: #2b2b2b;
    --paper: #ffffff;
    --stamp-grey: #8a8a8a;
    --rule: #555555;
  }
  html, body {
    margin: 0;
    padding: 0;
    width: 779px;
    height: 1200px;
    overflow: hidden;
    background: var(--paper);
  }
  .postcard {
    display: block;
    width: 779px;
    height: 1200px;
    font-family: "Arimo", Arial, sans-serif;
  }
  .body-text { fill: var(--paper); font-size: 19px; }
  .italic-claim { fill: var(--paper); font-size: 18px; font-weight: 700; font-style: italic; }
  .company-name { fill: var(--brand-blue); font-size: 17px; font-weight: 700; }
  .address-line { fill: var(--ink); font-size: 20px; }
  .email { fill: var(--ink); font-size: 19px; font-weight: 700; }
  .phone { fill: var(--brand-blue); font-size: 43px; font-weight: 700; font-style: italic; }
  .brand-name { fill: var(--logo-ink); font-weight: 400; }
  .service-item { fill: var(--paper); font-size: 18px; }
  .tick { stroke: var(--paper); stroke-width: 1.5; fill: none; }
  .stamp-text { fill: var(--paper); font-size: 16px; font-style: italic; }
  .address-rule { stroke: var(--rule); stroke-width: 1; stroke-dasharray: 2 2; }
</style>
</head>
<body>
<svg class="postcard" viewBox="0 0 779 1200" width="779" height="1200" xmlns="http://www.w3.org/2000/svg">
  <defs>
    <linearGradient id="kitchenLight" x1="0" y1="0" x2="0" y2="1">
      <stop offset="0" stop-color="#f3ecbf"/>
      <stop offset="0.55" stop-color="#c99a5a"/>
      <stop offset="1" stop-color="#b9894c"/>
    </linearGradient>
    <linearGradient id="kitchenDark" x1="0" y1="0" x2="0" y2="1">
      <stop offset="0" stop-color="#4a3223"/>
      <stop offset="0.5" stop-color="#8a5a32"/>
      <stop offset="1" stop-color="#3b2a1e"/>
    </linearGradient>
    <linearGradient id="blueBand" x1="0" y1="0" x2="1" y2="1">
      <stop offset="0" stop-color="#1f9ae0"/>
      <stop offset="1" stop-color="#0b66ad"/>
    </linearGradient>
    <linearGradient id="softRoom" x1="0" y1="0" x2="0" y2="1">
      <stop offset="0" stop-color="#e4ebf0"/>
      <stop offset="1" stop-color="#f7f8f9"/>
    </linearGradient>
  </defs>

  <!-- Front side -->
  <g class="front-side">
    <rect class="front-room" x="0" y="0" width="779" height="598" fill="url(#softRoom)" role="img" aria-label="Faint kitchen interior backdrop"/>
    <polygon class="hero-photo" points="0,0 456,0 306,598 0,598" fill="url(#kitchenLight)" role="img" aria-label="Photo of a bright kitchen with oak cabinets, granite countertop and a window over the sink"/>
    <polygon class="message-panel" points="456,0 779,0 779,352 364,388" fill="url(#blueBand)"/>

    <g class="brand-lockup">
      <text class="brand-name" x="52" y="66" font-size="40">BrambleWood</text>
      <text class="brand-name" x="322" y="94" font-size="26" text-anchor="end">Interiors</text>
    </g>

    <g class="intro-copy" text-anchor="end">
      <text class="body-text" x="743" y="60">If your tired of dealing with</text>
      <text class="body-text" x="743" y="85">unreliable contractors deal</text>
      <text class="body-text" x="743" y="110">with me. I'm so confident in my</text>
      <text class="body-text" x="743" y="135">work, here are the numbers to</text>
      <text class="body-text" x="743" y="160" font-weight="700" font-style="italic">previous customer.</text>
      <text class="body-text" x="743" y="209"><tspan font-weight="700">Mrs.Pelham:</tspan> 703-555-0142</text>
      <text class="body-text" x="743" y="236"><tspan font-weight="700">Mr.Castellano:</tspan> 703-555-0187</text>
    </g>

    <g class="claim" transform="rotate(-5 570 315)">
      <text class="italic-claim" x="402" y="297">They will tell you I can provide you</text>
      <text class="italic-claim" x="402" y="320">that dream kitchen and countertop</text>
      <text class="italic-claim" x="402" y="343">installed, within a week.</text>
    </g>

    <g class="discount-badge">
      <circle cx="356" cy="444" r="84" fill="#e3e3e3"/>
      <circle cx="356" cy="444" r="72" fill="#1a8fd6"/>
      <text x="350" y="452" fill="#ffffff" font-size="52" text-anchor="middle" transform="rotate(-22 350 440)">10%</text>
      <g transform="rotate(-18 360 478)">
        <rect x="286" y="462" width="150" height="30" fill="#0d6fb8"/>
        <text x="361" y="484" fill="#ffffff" font-size="18" font-weight="700" text-anchor="middle" letter-spacing="1">DISCOUNT</text>
      </g>
    </g>

    <g class="front-address" transform="rotate(-4 620 430)">
      <text class="company-name" x="505" y="414">BrambleWood Interiors llc</text>
      <text class="address-line" x="505" y="440">5819 fernwick dale CT</text>
      <text class="address-line" x="505" y="465">Falls church VA,22042</text>
    </g>
    <text class="email" x="465" y="509">Ovashtakar@mailbrook.net</text>
    <text class="phone" x="438" y="558">703-555-0163</text>
  </g>

  <rect class="side-divider" x="0" y="598" width="779" height="6" fill="#ffffff"/>

  <!-- Back side -->
  <g class="back-side">
    <rect x="0" y="604" width="779" height="596" fill="#ffffff"/>
    <rect class="back-room" x="0" y="1090" width="410" height="110" fill="url(#softRoom)" role="img" aria-label="Faint room backdrop"/>
    <rect class="back-room" x="410" y="1080" width="369" height="120" fill="url(#softRoom)"/>
    <rect class="showcase-photo" x="0" y="604" width="364" height="258" fill="url(#kitchenDark)" role="img" aria-label="Photo of a luxury kitchen with dark wood cabinets, granite island and pendant lights"/>
    <polygon class="services-band" points="0,862 364,862 404,1078 0,1110" fill="url(#blueBand)"/>
    <line x1="364" y1="604" x2="410" y2="1200" stroke="#e0e0e0" stroke-width="1"/>

    <g class="services-list">
      <path class="tick" d="M36 890 l4 5 l7 -10"/>
      <text class="service-item" x="64" y="896">granite and marble kitchen and</text>
      <text class="service-item" x="64" y="918">bathroom fabrication and install</text>
      <path class="tick" d="M36 948 l4 5 l7 -10"/>
      <text class="service-item" x="64" y="954">any flooring, hardwood, marble,</text>
      <text class="service-item" x="64" y="976">carpet, laminate, install</text>
      <path class="tick" d="M36 1006 l4 5 l7 -10"/>
      <text class="service-item" x="64" y="1012">Kitchen cabinet design and install</text>
      <path class="tick" d="M36 1042 l4 5 l7 -10"/>
      <text class="service-item" x="64" y="1048">Bathroom remodelling</text>
    </g>

    <g class="back-address" transform="rotate(-5 200 1120)">
      <text class="company-name" x="88" y="1112">BrambleWood Interiors llc</text>
      <text class="address-line" x="88" y="1138">5819 fernwick dale CT</text>
      <text class="address-line" x="88" y="1163">Falls church VA,22042</text>
    </g>

    <g class="postmark" fill="none" stroke="#8a8a8a" stroke-width="4" stroke-linecap="round">
      <path d="M560 678 q15 -8 30 0 t30 0 t30 0"/>
      <path d="M560 692 q15 -8 30 0 t30 0 t30 0"/>
      <path d="M560 706 q15 -8 30 0 t30 0 t30 0"/>
      <circle cx="690" cy="686" r="50" stroke-width="2"/>
    </g>
    <g class="stamp" transform="rotate(15 700 680)">
      <rect x="658" y="632" width="88" height="96" fill="#ffffff"/>
      <rect x="664" y="638" width="76" height="84" fill="#8a8a8a"/>
      <text class="stamp-text" x="678" y="662">Place</text>
      <text class="stamp-text" x="678" y="680">stamp</text>
      <text class="stamp-text" x="678" y="698">here</text>
    </g>

    <line class="address-rule" x1="458" y1="859" x2="760" y2="859"/>
    <line class="address-rule" x1="458" y1="912" x2="760" y2="912"/>
    <line class="address-rule" x1="458" y1="965" x2="760" y2="965"/>

    <text class="email" x="744" y="1120" text-anchor="end" font-size="18">Ovashtakar@mailbrook.net</text>
    <text class="phone" x="744" y="1163" text-anchor="end" font-size="40">703-555-0163</text>
  </g>
</svg>
</body>
</html>
```